Fieldstone Sporting
F.S.S. Sports
Project: Fieldstone Sporting
Fieldstone Sporting - Sports
Creative Brief
Use same font as used in my logo
Use your better judgement
Professional
Weston L. Barrow Jr.
CEO
Owings Mills, MD
W.barrow17@quillmail.example
www.FSSsports.example
Logo and web address
Concepts
Business card and stationary design. We provide umpires & referees for teams/organizations.

```html
<!DOCTYPE html>
<html lang="en">
<head>
<meta charset="utf-8">
<title>Fieldstone Sporting – Business Card</title>
<link rel="stylesheet" href="https://fonts.googleapis.com/css2?family=Tinos:wght@400;700&display=swap">
<style>
  :root {
    --backdrop: #3a3a3a;
    --card: #ffffff;
    --band-blue: #27549b;
    --accent-green: #7cc242;
    --ink: #3b3b3b;
    --icon-blue: #2f5fa8;
    --name-white: #ffffff;
  }
  html, body {
    margin: 0;
    padding: 0;
    overflow: hidden;
  }
  body {
    width: 1200px;
    height: 780px;
    background: var(--backdrop);
    font-family: "Tinos", "Times New Roman", serif;
    position: relative;
  }
  .business-card {
    position: absolute;
    left: 100px;
    top: 104px;
    width: 1000px;
    height: 572px;
    background: var(--card);
    border-radius: 34px;
    overflow: hidden;
    box-shadow: 0 10px 30px rgba(0,0,0,0.45);
  }
  .card-header-art {
    position: absolute;
    left: 0;
    top: 0;
    width: 1000px;
    height: 230px;
  }
  .holder {
    position: absolute;
    right: 52px;
    top: 30px;
    text-align: right;
    color: var(--name-white);
  }
  .holder-name {
    font-weight: 700;
    font-size: 34px;
    margin: 0;
    line-height: 1.1;
  }
  .holder-title {
    font-size: 21px;
    margin: 6px 0 0;
  }
  .brand {
    position: absolute;
    left: 150px;
    top: 230px;
    display: flex;
    align-items: center;
    gap: 18px;
  }
  .brand-dot {
    width: 26px;
    height: 26px;
    border-radius: 50%;
    background: var(--accent-green);
  }
  .brand-name {
    font-weight: 700;
    font-size: 50px;
    color: var(--band-blue);
    margin: 0;
    letter-spacing: 1px;
  }
  .address {
    position: absolute;
    left: 0;
    width: 1000px;
    top: 365px;
    text-align: center;
    font-size: 24px;
    color: var(--ink);
    margin: 0;
  }
  .contact-row {
    position: absolute;
    display: flex;
    align-items: center;
    gap: 28px;
    font-size: 23px;
    color: var(--ink);
  }
  .contact-row.primary { left: 360px; top: 430px; }
  .contact-row.secondary { left: 90px; top: 478px; }
  .contact-item {
    display: flex;
    align-items: center;
    gap: 8px;
  }
  .contact-icon {
    width: 22px;
    height: 22px;
    flex: none;
  }
</style>
</head>
<body>
  <article class="business-card">
    <svg class="card-header-art" viewBox="0 0 1000 230" aria-hidden="true">
      <path d="M0,0 H1000 V118 Q620,62 0,150 Z" fill="var(--band-blue)"/>
      <path d="M0,150 Q620,62 1000,118 V134 Q620,84 0,168 Z" fill="var(--accent-green)"/>
    </svg>

    <header class="holder">
      <h1 class="holder-name">Weston L. Barrow Jr.</h1>
      <p class="holder-title">CEO</p>
    </header>

    <div class="brand">
      <span class="brand-dot"></span>
      <p class="brand-name">Fieldstone Sporting</p>
    </div>

    <p class="address">P.O. Box Owings Mills, MD</p>

    <div class="contact-row primary">
      <span class="contact-item">
        <svg class="contact-icon" viewBox="0 0 24 24"><path d="M6 3 L10 7 L8 10 Q10 14 14 16 L17 14 L21 18 L18 21 Q8 20 3 6 Z" fill="var(--icon-blue)"/></svg>
        410-555-0182
      </span>
      <span class="contact-item">
        <svg class="contact-icon" viewBox="0 0 24 24"><rect x="6" y="2" width="12" height="20" rx="2" fill="var(--icon-blue)"/><rect x="8" y="5" width="8" height="11" fill="#fff"/></svg>
        410-555-0147
      </span>
    </div>

    <div class="contact-row secondary">
      <span class="contact-item">
        <svg class="contact-icon" viewBox="0 0 24 24"><rect x="7" y="3" width="10" height="7" fill="var(--icon-blue)"/><rect x="3" y="10" width="18" height="10" rx="2" fill="var(--icon-blue)"/><rect x="7" y="15" width="10" height="3" fill="#fff"/></svg>
        410-555-0163
      </span>
      <span class="contact-item">
        <svg class="contact-icon" viewBox="0 0 24 24"><circle cx="12" cy="12" r="10" fill="var(--icon-blue)"/><circle cx="12" cy="12" r="4" fill="none" stroke="#fff" stroke-width="2"/></svg>
        W.barrow17@quillmail.example
      </span>
      <span class="contact-item">
        <svg class="contact-icon" viewBox="0 0 24 24"><circle cx="12" cy="12" r="10" fill="var(--icon-blue)"/><ellipse cx="12" cy="12" rx="4" ry="10" fill="none" stroke="#fff" stroke-width="1.5"/><line x1="2" y1="12" x2="22" y2="12" stroke="#fff" stroke-width="1.5"/></svg>
        www.FSSsports.example
      </span>
    </div>
  </article>
</body>
</html>
```